Law Firm Web Design Project

I need a website design for my law firm. I have attached to this description the URL of a website I liked with a description of the elements of that website that appeal to me.

I am also attaching my law firm's logo, so you can review that design when you create the website design.

Reference Site: www.harborfamilycounselpros.com

What we like about this site:
• The different layers
• Subtle designs, textures, curves
• 3 dimensional
• Floating effect
• Simple logo that stands out (we are providing logo)
• Prominent phone number
• Location of Areas of Practice
oDivorce, Legal Separation, Paternity, Spousal Maintenance, Child Custody, Child Support, Protective Orders, Community Property, Business Evaluations
• The limited amount of links across the top
o Home, Meet Our Attorney, FAQ, Contact Us
• Request A Consultation click through
• Right side bar with the moving icons
• Badges

Other Tips:
• We don’t want the website to be dark. The logo can standout and the website can have its own colors and flow.
• We would like there to be a “call to action” or way to get in touch on every page and every page view
• We would like a place for credit card icons at the bottom of the page
• Strong, yet elegant
• Finally, just use the website provided as a guide. Explore different colors, textures, shapes, shadows etc.
Updates

I would prefer the website have colors that are complementary to my logo and that are strong and elegant.  I like black, gold, amber, and tan colors.  Black should be used sparingly as an accent only, since I don't want the website to be too dark.

Please review the website I provided as an example in my project description.  I really like the three dimensional aspects of that website (web page floating on top of a background and the logo in the upper left floating on top of the web page).  I also like the use of "swirling" on the background and the webpage.  I hope this additional information is helpful.

Requirements
Must have
• I need a place to insert "client testimonials", a place to insert four logos of awards the law firm has received, a place for people to fill out a form to contact the law firm via email, and a place for people to click to review articles I have written.

```html
<!DOCTYPE html>
<html lang="en">
<head>
<meta charset="utf-8">
<title>Alderwick Law</title>
<link rel="stylesheet" href="https://fonts.googleapis.com/css2?family=Old+Standard+TT:ital,wght@0,400;0,700;1,400&family=Questrial&display=swap">
<style>
:root{
  --bg:#e4d9c8;
  --page:#ffffff;
  --page-soft:#f3f1ee;
  --ink:#1c1a17;
  --text:#2e2b27;
  --muted:#5a544c;
  --gold:#b39a4c;
  --gold-light:#d9c27a;
  --gold-dark:#8d7432;
  --tan-line:#c9b49c;
  --nav:#151412;
  --rule:#cfc6ba;
}
*{box-sizing:border-box;margin:0;padding:0}
html,body{width:715px;height:1200px;overflow:hidden;background:var(--bg)}
body{position:relative;font-family:"Questrial",Arial,sans-serif;color:var(--text);font-size:9px}
.abs{position:absolute}
.page{left:30px;top:0;width:655px;height:973px;background:var(--page);box-shadow:0 0 12px rgba(0,0,0,.18)}
.header-top{left:30px;top:0;width:655px;height:50px;background:linear-gradient(#fff,#ece6dd)}
.phone{right:35px;top:20px;font-family:"Old Standard TT",serif;font-size:18px;color:var(--ink)}
.phone em{font-size:13px;font-weight:700}
.nav{left:30px;top:50px;width:655px;height:35px;background:linear-gradient(#2c2a27,var(--nav))}
.nav ul{list-style:none;display:flex;position:absolute;left:308px;top:11px}
.nav li{color:#fff;font-size:11px;margin-right:32px}
.hero{left:30px;top:85px;width:655px;height:277px;background:linear-gradient(100deg,#efe9b8 0%,#e9d89a 35%,#d7a968 60%,#e8d6bb 100%)}
.hero-title{left:52px;top:168px;font-family:"Old Standard TT",serif;font-weight:400;font-size:35px;line-height:34px;color:var(--ink)}
.hero-title span{display:block;padding-left:64px}
.cta{left:17px;top:283px;width:242px;height:43px;background:linear-gradient(#dcc57d,#b0933f);box-shadow:0 3px 6px rgba(0,0,0,.35);font-size:17px;color:#2c2614;text-align:center;line-height:43px}
.cta-fold{left:17px;top:273px}
.logo-tab{left:46px;top:0}
.logo-name{left:46px;top:30px;width:266px;text-align:center;font-family:"Old Standard TT",serif;font-size:25px;color:var(--gold-dark)}
.logo-since{left:46px;top:100px;width:266px;text-align:center;font-family:"Old Standard TT",serif;font-style:italic;font-size:13px;color:#8a857d}
.content-bg{left:30px;top:362px;width:655px;height:611px;background:linear-gradient(var(--page-soft),#fff 30%)}
.sidebar{left:30px;top:375px;width:161px;height:279px;background:linear-gradient(90deg,#eae4dc,#f2ede7);border-radius:0 0 8px 0;box-shadow:1px 2px 3px rgba(0,0,0,.12)}
.sidebar h3{background:linear-gradient(#34312d,#111);color:#fff;font-family:"Old Standard TT",serif;font-weight:400;font-size:13px;height:35px;line-height:35px;padding-left:20px;border-radius:0 6px 0 0}
.practice{list-style:none;margin:7px 12px 0 11px}
.practice li{font-size:10px;color:var(--text);padding:5px 0 6px 10px;border-bottom:1px dotted #b9ada0}
.badge{background:#d8d2c8}
.intro-h{left:221px;top:380px;font-family:"Old Standard TT",serif;font-weight:400;font-size:17px;color:var(--ink)}
.para{font-size:9.6px;line-height:11px;color:var(--text)}
.intro-p{left:221px;top:406px;width:443px}
.divider{height:3px;background:var(--tan-line)}
.link{font-size:9.5px;color:var(--ink);text-decoration:underline}
.arrow{width:0;height:0;border-left:6px solid var(--ink);border-top:4px solid transparent;border-bottom:4px solid transparent}
.articles-h{left:221px;top:501px;font-family:"Old Standard TT",serif;font-weight:400;font-size:18px;color:var(--ink)}
.thumb{width:142px;height:70px;border:4px solid #fff;box-shadow:0 2px 4px rgba(0,0,0,.3)}
.art-title{font-weight:700;font-size:9px;color:var(--ink)}
.art-date{font-size:8px;color:var(--ink)}
.art-p{width:142px;font-size:8.6px;line-height:10px}
.testimonial{left:220px;top:768px;width:447px;height:155px;background:linear-gradient(#f6f4f1,#ecebe8);box-shadow:0 4px 7px rgba(0,0,0,.3)}
.testimonial h3{position:absolute;left:15px;top:12px;font-family:"Old Standard TT",serif;font-weight:400;font-size:17px;color:var(--ink)}
.quote{left:15px;top:37px;width:418px;font-style:italic;font-size:9.8px;line-height:11px}
.footer-nav{left:15px;top:989px;font-size:8.6px;color:var(--ink)}
.copy{left:17px;top:1012px;font-size:8.6px;line-height:14px;color:var(--ink)}
.copy b{font-family:"Old Standard TT",serif}
.card{width:35px;height:21px;border-radius:2px;font-size:7px;color:#fff;text-align:center;line-height:21px}
.social{font-size:8px;color:var(--ink)}
.social i{display:inline-block;width:9px;height:9px;background:var(--gold-dark);margin-right:3px;vertical-align:-1px}
.vline{left:507px;top:990px;width:1px;height:196px;background:#bfb3a3}
.qc-h{right:9px;top:988px;font-family:"Old Standard TT",serif;font-weight:700;font-size:10px;color:var(--ink)}
.field{left:541px;width:161px;height:18px;background:linear-gradient(#fff,#f1f1f1);border:1px solid #cfcac2;border-radius:3px;font-size:8.5px;padding:3px 7px;color:var(--ink)}
.send{left:653px;top:1162px;width:49px;height:17px;background:linear-gradient(#f6f6f6,#cfcfcf);border-radius:3px;font-size:8.5px;font-weight:700;text-align:center;line-height:17px;color:var(--ink)}
.bottom-bar{left:0;top:1196px;width:715px;height:4px;background:#4a433b}
</style>
</head>
<body>
<div class="abs page"></div>
<div class="abs header-top"></div>
<div class="abs phone"><em>Call Us</em> (555) 318.2046</div>
<nav class="abs nav"><ul><li>Home</li><li>Meet Our Attorney</li><li>FAQ</li><li>Contact Us</li></ul></nav>

<div class="abs hero" role="img" aria-label="Sunlit photo of a smiling mother hugging her young child outdoors"></div>
<h1 class="abs hero-title">Let us solve<span>your problem</span></h1>
<svg class="abs cta-fold" width="14" height="12"><polygon points="14,0 14,12 0,12" fill="#5b4a1e"/></svg>
<div class="abs cta">Request a Consultation</div>

<svg class="abs logo-tab" width="266" height="144" viewBox="0 0 266 144">
  <polygon points="4,0 262,0 262,104 133,140 4,104" fill="#555" opacity=".35"/>
  <polygon points="8,0 258,0 258,100 133,134 8,100" fill="#f8f7f4" stroke="#3a3835" stroke-width="6"/>
  <line x1="20" y1="84" x2="246" y2="84" stroke="#e3dfd8" stroke-width="1"/>
</svg>
<div class="abs logo-name">Alderwick Law</div>
<div class="abs logo-since">Since 2000</div>

<div class="abs content-bg"></div>

<aside class="abs sidebar">
  <h3>Areas Of Practice</h3>
  <ul class="practice">
    <li>Divorce</li><li>Legal Separation</li><li>Paternity</li><li>Spousal Maintenance</li><li>Child Custody</li><li>Child Support</li><li>Protective Orders</li><li>Community Property</li><li>Business Evaluations</li>
  </ul>
</aside>
<div class="abs badge" style="left:86px;top:676px;width:51px;height:84px;border-radius:3px" role="img" aria-label="Accredited business badge"></div>
<div class="abs badge" style="left:54px;top:785px;width:112px;height:50px;border-radius:3px" role="img" aria-label="Peer review rating badge"></div>
<div class="abs badge" style="left:67px;top:864px;width:92px;height:64px;border-radius:3px" role="img" aria-label="Top ten solo practitioners award badge"></div>

<h2 class="abs intro-h">Alderwick Law provide nationwide legal services.</h2>
<p class="abs para intro-p">Lorem ipsum dolor sit amet, consectetur adipisicing elit, sed do eiusmod tempor incididunt ut labore et dolore magna aliqua. Ut enim ad minim veniam, quis nostrud exercitation ullamco laboris nisi ut aliquip ex ea commodo consequat. Duis aute irure dolor in reprehenderit in voluptate velit esse cillum dolore eu fugiat nulla pariatur. Excepteur sint occaecat cupidatat non proident, sunt in culpa qui officia deserunt mollit anim id est laborum.</p>
<div class="abs divider" style="left:221px;top:480px;width:328px"></div>
<span class="abs link" style="left:562px;top:476px">Learn More About Us</span>
<div class="abs arrow" style="left:662px;top:477px"></div>

<h2 class="abs articles-h">Articles</h2>
<div class="abs thumb" style="left:221px;top:531px;background:linear-gradient(#c9621c,#7a2d0c)" role="img" aria-label="Gavel and scales of justice"></div>
<div class="abs thumb" style="left:374px;top:531px;background:linear-gradient(90deg,#5c3b1c,#b08a45,#4a2e15)" role="img" aria-label="Row of leather law books"></div>
<div class="abs thumb" style="left:528px;top:531px;background:linear-gradient(135deg,#dfe7ef,#9fb2c5)" role="img" aria-label="Pen resting on a document"></div>

<div class="abs" style="left:221px;top:610px"><div class="art-title">Lorem ipsum dolor sit amet</div><div class="art-date">March 16, 2012</div></div>
<div class="abs" style="left:374px;top:610px"><div class="art-title">Lorem ipsum dolor sit amet</div><div class="art-date">March 16, 2012</div></div>
<div class="abs" style="left:528px;top:610px"><div class="art-title">Lorem ipsum dolor sit amet</div><div class="art-date">March 16, 2012</div></div>
<p class="abs para art-p" style="left:221px;top:641px">Consectetur adipisicing elit, sed do eiusmod tempor incididunt ut labore et dolore magna aliqua. Ut enim ad minim veniam, quis nostrud exercitation ullamco laboris nisi ut aliquip ex ea commodo consequat.</p>
<p class="abs para art-p" style="left:374px;top:641px">Consectetur adipisicing elit, sed do eiusmod tempor incididunt ut labore et dolore magna aliqua. Ut enim ad minim veniam, quis nostrud exercitation ullamco laboris nisi ut aliquip ex ea commodo consequat.</p>
<p class="abs para art-p" style="left:528px;top:641px">Consectetur adipisicing elit, sed do eiusmod tempor incididunt ut labore et dolore magna aliqua. Ut enim ad minim veniam, quis nostrud exercitation ullamco laboris nisi ut aliquip ex ea commodo consequat.</p>
<span class="abs link" style="left:316px;top:710px">Read More</span>
<span class="abs link" style="left:469px;top:710px">Read More</span>
<span class="abs link" style="left:622px;top:710px">Read More</span>

<div class="abs divider" style="left:221px;top:743px;width:328px"></div>
<span class="abs link" style="left:562px;top:739px">Review More Articles</span>
<div class="abs arrow" style="left:662px;top:740px"></div>

<section class="abs testimonial">
  <h3>Client Testimonial</h3>
  <p class="abs quote">“Lorem ipsum dolor sit amet, consectetur adipisicing elit, sed do eiusmod tempor incididunt ut labore et dolore magna aliqua. Ut enim ad minim veniam, quis nostrud exercitation ullamco laboris nisi ut aliquip ex ea commodo consequat. Duis aute irure dolor in reprehenderit in voluptate velit esse cillum dolore eu fugiat nulla pariatur. Excepteur sint occaecat cupidatat non proident, sunt in culpa qui officia deserunt mollit anim id est laborum.”</p>
  <div class="abs" style="right:16px;top:102px;font-weight:700;font-size:9.5px">-Dana Reyes</div>
  <span class="abs link" style="left:330px;top:133px">Read All Testimonials</span>
  <div class="abs arrow" style="left:432px;top:134px"></div>
</section>

<div class="abs footer-nav">Home &nbsp;|&nbsp; Meet Our Attorney &nbsp;|&nbsp; FAQ &nbsp;|&nbsp; Contact Us</div>
<div class="abs copy"><b>© 2012 Alderwick Law</b><br>48 Harbor Lane 30512 Eastbrook<br>Tél : 05 55 21 84 30 &nbsp;&nbsp;&nbsp; Fax : 05 55 21 84 30</div>
<div class="abs social" style="left:17px;top:1062px"><span><i></i>Profilo</span> &nbsp;<span><i></i>Chatter</span> &nbsp;<span><i></i>Circlo</span></div>
<div class="abs card" style="left:303px;top:990px;background:#6a8aa8">Paywell</div>
<div class="abs card" style="left:340px;top:990px;background:#7d7466">Cardline</div>
<div class="abs card" style="left:377px;top:990px;background:#8a5a3a">Meridian</div>
<div class="abs card" style="left:414px;top:990px;background:#a48a55">Northpay</div>

<div class="abs vline"></div>
<div class="abs qc-h">Quick Contact</div>
<div class="abs field" style="top:1009px">Name:</div>
<div class="abs field" style="top:1030px">Email:</div>
<div class="abs field" style="top:1051px">Phone:</div>
<div class="abs field" style="top:1072px;height:83px">Message:</div>
<div class="abs send">Send</div>
<div class="abs bottom-bar"></div>
</body>
</html>
```